Flyer-Design für Unkrautbekämpfung
Sehr gute und nette Zusammenarbeit. Auch auf Änderungswünsche nach Beendigung der Contest-Phase wurde schnell eingegangen. Gerne wieder, sehr zu empfehlen!
Zielgruppe
Unkrautbekämpfung mit dem Heißwasser-Schaum-System. In Eigenleistung und Vermietung des Geräts.
Zielgruppe: Privatleute mit eigenem Grundstück, Landwirte, kleine Geschäfte (Restaurants, Läden mit Parkplatz etc.)
Aufgabenstellung
Link zur Website: www.beetglanz-service.net
Der Kreativität sind keine Grenzen gesetzt.
Bitte Vorder- und Rückseite designen. Auf der Rückseite können hauptsächlich Kontaktinformationen sein.

```html
<!DOCTYPE html>
<html lang="de">
<head>
<meta charset="utf-8">
<title>Beetglanz – Flyer Vorder- und Rückseite</title>
<link rel="stylesheet" href="https://fonts.googleapis.com/css2?family=Montserrat:ital,wght@0,400;0,500;0,700;0,800;1,400&display=swap">
<style>
  :root{
    --bg:#ebebeb;
    --paper:#ffffff;
    --green:#5cb648;
    --green-light:#7cc96a;
    --green-dark:#2f7d32;
    --blue:#2a6f93;
    --blue-light:#3f95b8;
    --text-green:#3c8a2e;
  }
  *{box-sizing:border-box;margin:0;padding:0}
  html,body{width:1200px;height:2196px;overflow:hidden;background:var(--bg)}
  body{position:relative;font-family:"Montserrat",sans-serif;color:var(--text-green)}
  .flyer{position:absolute;left:265px;width:668px;height:943px;background:var(--paper);overflow:hidden;box-shadow:0 18px 24px -14px rgba(0,0,0,.25)}
  .flyer--front{top:86px}
  .flyer--back{top:1163px}
  .waves{position:absolute;inset:0;width:668px;height:943px}
  .abs{position:absolute}

  .top-bar{left:0;top:0;width:668px;height:10px;background:linear-gradient(90deg,var(--green-light),var(--green-dark))}
  .brand{display:flex;align-items:center;gap:10px}
  .brand__mark{width:34px;height:34px;background:var(--green)}
  .brand__name{font-weight:500;font-size:20px;color:var(--green-dark);line-height:1}
  .brand__sub{font-size:12.5px;color:#333;margin-top:3px}
  .brand--front{left:200px;top:26px}
  .brand--back{left:80px;top:479px}

  .badge{left:522px;top:28px;width:116px;height:116px;border-radius:50%;background:var(--green);border:5px solid #fff;box-shadow:0 0 0 2px var(--green)}

  .photo{top:108px;width:248px;height:172px}
  .photo--before{left:59px;background:linear-gradient(160deg,#9a9a94,#6f7563 50%,#58603f)}
  .photo--after{left:362px;background:linear-gradient(160deg,#c9c9c6,#4a4b4d 45%,#2e2f31)}
  .pill{left:68px;top:58px;width:124px;height:32px;border-radius:8px;background:rgba(108,190,80,.92);color:#fff;font-style:italic;font-size:24px;text-align:center;line-height:32px}

  .headline{left:158px;top:322px;font-weight:800;font-size:33px;line-height:32px;color:var(--green);white-space:nowrap}
  .subline{left:158px;top:400px;font-size:21px;color:var(--green);white-space:nowrap}
  .band-title{left:236px;top:447px;font-weight:700;font-size:24px;color:#fff;transform:rotate(2deg);white-space:nowrap}

  .benefits{left:151px;top:500px;list-style:none}
  .benefits li{display:flex;align-items:center;height:41px;font-style:italic;font-size:26px;color:var(--green-dark);white-space:nowrap}
  .benefits svg{width:32px;height:30px;margin-right:14px}
  .intro{left:143px;top:668px;width:410px;font-size:14px;line-height:26px;color:var(--green-dark);white-space:nowrap;letter-spacing:-.1px}

  .deco-trees{width:60px;height:160px;background:linear-gradient(180deg,var(--green-light),var(--green-dark))}
  .deco-trees--front{left:608px;top:643px;clip-path:polygon(100% 0,100% 100%,0 100%)}
  .deco-trees--back{left:0;top:649px;height:150px;clip-path:polygon(0 0,100% 100%,0 100%)}

  .web{left:164px;top:880px;display:flex;align-items:center;gap:10px}
  .web svg{width:30px;height:30px}
  .web__url{font-weight:800;font-size:22px;color:var(--green-dark);letter-spacing:-.3px;white-space:nowrap}
  .tagline{left:205px;top:910px;font-size:13px;color:#fff;white-space:nowrap}

  .hero{left:0;top:0;width:668px;height:440px;background:linear-gradient(170deg,#8aa06a,#4e6e3a 40%,#c9d7c6 60%,#3d5a2c)}
  .callout{left:46px;top:29px;width:114px;height:96px;border:2px solid #fff;border-radius:4px;padding:10px 8px;color:#fff;font-weight:500;font-size:19px;line-height:23px}
  .callout::after{content:"";position:absolute;right:6px;bottom:-14px;border-left:12px solid transparent;border-top:14px solid #fff}

  .contact-title{left:80px;top:554px;font-weight:800;font-size:32px;line-height:32px;color:var(--green);white-space:nowrap}
  .illus{left:392px;top:499px;width:276px;height:230px;background:linear-gradient(135deg,#e2f3dd,#f7f7f7 60%,#e6e9f1)}
  .contact{left:178px;font-size:14px;white-space:nowrap}
  .contact--phone{top:666px;display:grid;grid-template-columns:23px 82px auto;row-gap:2px;align-items:center}
  .contact--mail{top:730px;display:flex;align-items:center;gap:8px}
  .contact b{font-weight:700;color:var(--text-green)}
  .contact i{color:var(--green)}
  .contact svg{width:15px;height:17px}

  .footer{top:890px;color:#fff;font-size:12px;line-height:16px;white-space:nowrap}
  .footer--owner{left:140px}
  .footer--address{left:456px}
</style>
</head>
<body>

<section class="flyer flyer--front">
  <div class="abs photo photo--before" role="img" aria-label="Foto: Pflasterweg mit Unkraut vor der Behandlung">
    <div class="abs pill">Vorher</div>
  </div>
  <div class="abs photo photo--after" role="img" aria-label="Foto: sauberer Pflasterweg nach der Behandlung">
    <div class="abs pill">Nachher</div>
  </div>

  <svg class="waves" viewBox="0 0 668 943" aria-hidden="true">
    <defs>
      <linearGradient id="gBlue" x1="0" x2="1"><stop offset="0" stop-color="#2a6f93"/><stop offset="1" stop-color="#3f95b8"/></linearGradient>
      <linearGradient id="gGreen" x1="0" x2="1"><stop offset="0" stop-color="#7cc96a"/><stop offset="1" stop-color="#2f7d32"/></linearGradient>
      <linearGradient id="gGreenR" x1="0" x2="1"><stop offset="0" stop-color="#2f7d32"/><stop offset="1" stop-color="#7cc96a"/></linearGradient>
    </defs>
    <path d="M0 360 C160 288 380 272 668 250 L668 943 L0 943Z" fill="#fff"/>
    <path d="M0 240 C25 225 45 212 59 205 L59 235 C35 248 15 262 0 275Z" fill="url(#gGreenR)"/>
    <path d="M668 210 C640 222 622 232 610 240 L610 272 C630 258 648 250 668 245Z" fill="url(#gGreen)"/>
    <path d="M0 340 C150 272 370 262 668 232 L668 258 C380 286 170 298 0 372Z" fill="url(#gBlue)"/>
    <path d="M0 545 C70 470 210 446 400 443 C520 441 600 432 668 424 L668 488 C580 487 480 481 380 479 C220 477 90 495 0 580Z" fill="url(#gGreen)"/>
    <path d="M0 705 C70 790 220 832 420 828 C540 824 620 808 668 800 L668 836 C600 845 520 862 400 866 C220 872 70 840 0 760Z" fill="url(#gBlue)"/>
    <path d="M0 800 C110 860 300 890 668 858 L668 943 L0 943Z" fill="url(#gGreen)"/>
  </svg>

  <div class="abs top-bar"></div>
  <div class="abs brand brand--front">
    <div class="brand__mark"></div>
    <div><div class="brand__name">Beetglanz</div><div class="brand__sub">Biologische Unkrautvernichtung</div></div>
  </div>
  <div class="abs badge"></div>

  <h1 class="abs headline">Unkrautbekämpfung<br>&amp; Flächenpflege</h1>
  <p class="abs subline">Heißwasser-/Ökoschaum-Verfahren</p>
  <p class="abs band-title">Ökologie und Umwelt</p>

  <ul class="abs benefits">
    <li><svg viewBox="0 0 34 32"><path d="M2 17 L12 29 L32 2" fill="none" stroke="#2f7d32" stroke-width="5" stroke-linecap="round"/></svg>100% biologisch abbaubar</li>
    <li><svg viewBox="0 0 34 32"><path d="M2 17 L12 29 L32 2" fill="none" stroke="#2f7d32" stroke-width="5" stroke-linecap="round"/></svg>umweltfreundlich</li>
    <li><svg viewBox="0 0 34 32"><path d="M2 17 L12 29 L32 2" fill="none" stroke="#2f7d32" stroke-width="5" stroke-linecap="round"/></svg>nicht gesundheitsschädlich</li>
    <li><svg viewBox="0 0 34 32"><path d="M2 17 L12 29 L32 2" fill="none" stroke="#2f7d32" stroke-width="5" stroke-linecap="round"/></svg>optimale Denkmalpflege</li>
  </ul>

  <p class="abs intro">Mit dem Heißwasser- /Heißwasser-Schaumverfahren<br>wird nachhaltig Unkraut unter strikter Beachtung des<br>Pflanzenschutzgesetzes umweltfreundlich, effizient<br>und rein ökologisch beseitigt.</p>

  <div class="abs deco-trees deco-trees--front" role="img" aria-label="Dekorative Tannen-Silhouetten"></div>

  <div class="abs web">
    <svg viewBox="0 0 32 32"><g fill="none" stroke="#2f7d32" stroke-width="2"><circle cx="16" cy="16" r="13"/><ellipse cx="16" cy="16" rx="6" ry="13"/><path d="M3 16h26M5 9h22M5 23h22"/></g></svg>
    <span class="web__url">www.beetglanz-service.net</span>
  </div>
  <p class="abs tagline">leistungsstark · wirtschaftlich günstig · ökologisch</p>
</section>

<section class="flyer flyer--back">
  <div class="abs hero" role="img" aria-label="Foto: Schaumbehandlung von Unkraut zwischen Erdbeerpflanzen"></div>
  <div class="abs illus" role="img" aria-label="Illustration: Person behandelt Unkraut mit Schaumgerät"></div>
  <svg class="waves" viewBox="0 0 668 943" aria-hidden="true">
    <defs>
      <linearGradient id="bBlue" x1="0" x2="1"><stop offset="0" stop-color="#2a6f93"/><stop offset="1" stop-color="#3f95b8"/></linearGradient>
      <linearGradient id="bGreen" x1="0" x2="1"><stop offset="0" stop-color="#7cc96a"/><stop offset="1" stop-color="#2f7d32"/></linearGradient>
    </defs>
    <path d="M0 305 C150 360 400 330 668 388 L668 499 L392 499 L392 729 L668 729 L668 943 L0 943Z" fill="#fff"/>
    <path d="M0 318 C200 372 450 332 668 410 L668 442 C450 364 200 402 0 350Z" fill="url(#bGreen)"/>
    <path d="M0 372 C200 412 450 382 668 470 L668 500 C450 414 200 442 0 396Z" fill="url(#bGreen)"/>
    <path d="M0 820 C200 790 500 830 668 700 L668 742 C500 862 200 832 0 860Z" fill="url(#bGreen)"/>
    <path d="M0 868 C200 832 450 880 668 842 L668 943 L0 943Z" fill="url(#bBlue)"/>
  </svg>

  <div class="abs callout">Unkraut ohne Gift im Griff</div>

  <div class="abs brand brand--back">
    <div class="brand__mark"></div>
    <div><div class="brand__name">Beetglanz</div><div class="brand__sub">Biologische Unkrautvernichtung</div></div>
  </div>

  <h2 class="abs contact-title">Sprechen Sie<br>uns einfach an:</h2>

  <div class="abs contact contact--phone">
    <svg viewBox="0 0 16 18"><rect x="3" y="1" width="10" height="16" rx="2" fill="none" stroke="#2a6f93" stroke-width="1.6"/></svg>
    <b>Festnetz :</b><i>05021 - 4836</i>
    <span></span><b>Mobil:</b><i>0171-5520394</i>
  </div>
  <div class="abs contact contact--mail">
    <svg viewBox="0 0 16 18"><rect x="1" y="4" width="14" height="10" fill="none" stroke="#2a6f93" stroke-width="1.6"/><path d="M1 4l7 6 7-6" fill="none" stroke="#2a6f93" stroke-width="1.6"/></svg>
    <b>info@beetglanz-service.net</b>
  </div>

  <div class="abs deco-trees deco-trees--back" role="img" aria-label="Dekorative Tannen-Silhouetten"></div>

  <p class="abs footer footer--owner">Beetglanz - Biologische Unkrautvernichtung<br>Inh. Torben Hallweg</p>
  <p class="abs footer footer--address">Lindenweg 14<br>31600 Feldhagen</p>
</section>

</body>
</html>
```